Architecture firm needing a business card

We need a business card design for a new company based in the US called "Dorrance Architecture". Seeking minimalist designs that have a creativity/design feel but must be clean and professional. Please refer to the logo attached.

Target Market(s)

Real Estate Investors, Home Builders and Construction Firms.

Industry/Entity Type

Architecture

Contact Information for Business Card

Standard US size business cards. Would like to have some sort of graphic on the back side of the card - nothing that is too loud but something that may catch your attention. More or less grayscale colors that are in line with the logo colors (navy and greys essentially). Additional colors maybe accepted if blended properly (earthtones), but might be difficult to accomplish and maintain the clean/minimalist look.

Requirements
Must have
• Clean Lines
Nice to have
• some sort of graphics, would like to have something creative on the back side of the card
Should not have
• nothing too busy, cluttered or overwhelming.

```html
<!DOCTYPE html>
<html lang="en">
<head>
<meta charset="utf-8">
<title>Dorrance Architecture – Business Card</title>
<link href="https://fonts.googleapis.com/css2?family=Arimo:wght@400;700&display=swap" rel="stylesheet">
<style>
  :root {
    --navy: #1f4672;
    --grey: #a3a3a3;
    --text-grey: #9b9b9b;
    --ink: #3a3a3a;
    --paper: #ffffff;
    --backdrop: #e4e5e8;
  }
  * { box-sizing: border-box; margin: 0; padding: 0; }
  html, body { width: 1200px; height: 750px; overflow: hidden; }
  body {
    background: var(--backdrop);
    font-family: "Arimo", Arial, sans-serif;
    position: relative;
  }
  .card {
    position: absolute;
    top: 220px;
    width: 540px;
    height: 309px;
    box-shadow: 0 10px 28px rgba(0,0,0,0.18);
    overflow: hidden;
  }
  .wordmark {
    font-weight: 400;
    text-transform: uppercase;
    letter-spacing: 3px;
  }
  .wordmark span { display: block; }

  /* Front side */
  .card-front { left: 40px; background: var(--navy); color: var(--paper); }
  .card-front .wordmark {
    position: absolute;
    left: 0; right: 0; top: 92px;
    text-align: center;
    font-size: 30px;
    line-height: 36px;
    color: var(--paper);
  }
  .card-front .web {
    position: absolute;
    left: 0; right: 0; top: 238px;
    text-align: center;
    font-size: 11px;
    letter-spacing: 6px;
    color: var(--paper);
  }

  /* Back side */
  .card-back { left: 620px; background: var(--paper); }
  .band { position: absolute; left: 0; width: 60px; height: 18px; }
  .band-navy { top: 80px; background: var(--navy); }
  .band-grey { top: 100px; background: var(--grey); }
  .card-back .wordmark {
    position: absolute;
    left: 74px; top: 70px;
    font-size: 20px;
    line-height: 24px;
    color: var(--navy);
  }
  .holder {
    position: absolute;
    right: 40px; top: 66px;
    text-align: right;
  }
  .holder .name { font-size: 17px; font-weight: 700; color: var(--navy); }
  .holder .role { font-size: 12px; color: var(--text-grey); margin-top: 3px; }
  .address {
    position: absolute;
    left: 150px; top: 134px;
    font-size: 11.5px;
    line-height: 15px;
    font-style: normal;
    color: var(--ink);
  }
  .contacts {
    position: absolute;
    left: 150px; top: 174px;
    list-style: none;
    font-size: 11.5px;
    color: var(--ink);
  }
  .contacts li {
    display: flex;
    align-items: center;
    gap: 8px;
    height: 18px;
  }
  .contacts svg { width: 12px; height: 12px; fill: var(--navy); flex: none; }
</style>
</head>
<body>

<section class="card card-front" aria-label="Card front">
  <div class="wordmark"><span>Dorrance</span><span>Architecture</span></div>
  <div class="web">www.dorrancearch.com</div>
</section>

<section class="card card-back" aria-label="Card back">
  <div class="band band-navy"></div>
  <div class="band band-grey"></div>
  <div class="wordmark"><span>Dorrance</span><span>Architecture</span></div>

  <div class="holder">
    <div class="name">Elliot Marsh</div>
    <div class="role">President</div>
  </div>

  <address class="address">
    4127 Harbor Crest Lane<br>
    Millbrook, NY 12545
  </address>

  <ul class="contacts">
    <li>
      <svg viewBox="0 0 12 12" aria-hidden="true"><path d="M1 4c0-2 2-3 5-3s5 1 5 3l-2 1-1-1.5H4L3 5 1 4zM3 6h6l1 5H2l1-5zm3 1.2a1.3 1.3 0 100 2.6 1.3 1.3 0 000-2.6z"/></svg>
      <span>845 3102 7719</span>
    </li>
    <li>
      <svg viewBox="0 0 12 12" aria-hidden="true"><path d="M3 0h6a1 1 0 011 1v10a1 1 0 01-1 1H3a1 1 0 01-1-1V1a1 1 0 011-1zm.6 1.5v7.5h4.8V1.5H3.6zM6 9.8a.6.6 0 100 1.2.6.6 0 000-1.2z"/></svg>
      <span>845 6620 1487</span>
    </li>
    <li>
      <svg viewBox="0 0 12 12" aria-hidden="true"><path d="M3 0h5l1 1v3H3V0zM1 5h10a1 1 0 011 1v4a1 1 0 01-1 1H1a1 1 0 01-1-1V6a1 1 0 011-1zm2 2v1h6V7H3z"/></svg>
      <span>845 2290 6631</span>
    </li>
    <li>
      <svg viewBox="0 0 12 12" aria-hidden="true"><path d="M0 2h12v1L6 7 0 3V2zm0 2.4l6 4 6-4V10H0V4.4z"/></svg>
      <span>elliot@dorrancearch.com</span>
    </li>
    <li>
      <svg viewBox="0 0 12 12" aria-hidden="true"><path d="M6 0a6 6 0 100 12A6 6 0 006 0zm0 1.2c.8 0 1.7 1.6 1.9 4.2H4.1C4.3 2.8 5.2 1.2 6 1.2zM4.1 6.6h3.8C7.7 9.2 6.8 10.8 6 10.8S4.3 9.2 4.1 6.6z"/></svg>
      <span>www.dorrancearch.com</span>
    </li>
  </ul>
</section>

</body>
</html>
```